The Wellness Barn Business Card

Info for the front..... (in whichever order and layout looks best)
Carla Penhallow
Physiotherapist
4/37 Upper Creekbank Rd
Tallowbrook
QLD 4712
0462305178
carlapenhallow57@mailbox.example
www.thewellnessbarn.example.au
on the back I would like to be able to write appointments so probably just that heading with lines.
I like a sort of rustic style but mostly professional, colours in naturals, beige, brown, green etc. I dont mind if the logo colour is changed slightly to suit.

```html
<!DOCTYPE html>
<html lang="en">
<head>
<meta charset="utf-8">
<title>The Wellness Barn Business Card</title>
<link href="https://fonts.googleapis.com/css2?family=Poppins:wght@300;400;600;700;800&display=swap" rel="stylesheet">
<style>
  :root {
    --barn-green: #2d4a1f;
    --barn-green-deep: #223a16;
    --paper: #f4f4f1;
    --backdrop: #e9e8e5;
    --field: #f1f1ee;
    --ink-light: #ffffff;
  }
  * { margin: 0; padding: 0; box-sizing: border-box; }
  html, body {
    width: 1200px; height: 801px; overflow: hidden;
    background: var(--backdrop);
    font-family: "Poppins", sans-serif;
  }
  .sheet {
    position: relative; width: 1200px; height: 801px;
    display: flex; align-items: center; justify-content: center; gap: 40px;
  }
  .card {
    position: relative; width: 540px; height: 309px; overflow: hidden;
    background: var(--barn-green);
    box-shadow: 0 10px 24px rgba(0,0,0,0.18);
  }
  .card-front__art { position: absolute; inset: 0; }

  .brand-name {
    position: absolute; left: 34px; top: 96px; width: 220px;
    display: flex; align-items: center; gap: 12px;
    color: var(--ink-light); font-weight: 700; font-size: 28px; line-height: 1.05;
  }
  .brand-name__dot {
    flex: none; width: 18px; height: 18px; border-radius: 50%;
    background: var(--ink-light);
  }

  .identity {
    position: absolute; right: 26px; top: 22px; text-align: right; color: var(--ink-light);
  }
  .identity__name { font-weight: 700; font-size: 15px; letter-spacing: 0.5px; text-transform: uppercase; line-height: 1.4; }
  .identity__role { font-weight: 300; font-size: 11.5px; line-height: 1.4; }
  .identity__address { font-weight: 300; font-size: 11px; line-height: 1.4; margin-top: 14px; }

  .contacts {
    position: absolute; right: 18px; bottom: 20px; list-style: none;
    color: var(--barn-green); font-size: 10.5px; font-weight: 400;
  }
  .contacts__item { display: flex; justify-content: flex-end; align-items: center; gap: 7px; line-height: 1.75; }
  .contacts__icon { width: 12px; height: 12px; flex: none; }

  .card-back { background: linear-gradient(160deg, var(--barn-green) 0%, var(--barn-green-deep) 100%); color: var(--ink-light); }
  .appt-heading {
    position: absolute; left: 30px; top: 30px; right: 30px;
    display: flex; align-items: center; gap: 14px;
    font-weight: 800; font-size: 28px; letter-spacing: 1px;
  }
  .appt-heading__rule { flex: 1; height: 1px; background: rgba(255,255,255,0.7); margin-top: 6px; }
  .appt-row { position: absolute; display: flex; align-items: center; gap: 8px; }
  .appt-label { font-weight: 600; font-size: 13px; text-transform: uppercase; white-space: nowrap; }
  .appt-field { height: 28px; border-radius: 5px; background: var(--field); }
  .appt-row--name { left: 30px; right: 30px; top: 96px; }
  .appt-row--name .appt-field { flex: 1; }
  .appt-row--when { left: 30px; right: 30px; top: 146px; }
  .appt-row--when .appt-field { flex: 1; }
  .appt-row--when .appt-label--time { margin-left: 14px; }
  .day-list {
    position: absolute; left: 30px; right: 30px; bottom: 40px;
    display: flex; justify-content: space-between; list-style: none;
    font-size: 13px; font-weight: 400;
  }
  .day-list__item { display: flex; align-items: center; gap: 6px; }
  .day-list__box { width: 13px; height: 13px; border: 1.6px solid var(--ink-light); }
</style>
</head>
<body>
<main class="sheet">

  <section class="card card-front" aria-label="Business card front">
    <svg class="card-front__art" viewBox="0 0 540 309" preserveAspectRatio="none" aria-hidden="true">
      <path d="M40 309 C170 300 250 215 330 180 C410 146 470 138 540 134 L540 309 Z" fill="var(--paper)"/>
      <path d="M68 309 C190 298 262 222 340 190 C415 158 472 151 540 148" fill="none" stroke="var(--barn-green)" stroke-width="7"/>
      <path d="M92 309 C210 298 278 230 350 201 C422 171 476 163 540 161" fill="none" stroke="var(--barn-green)" stroke-width="5"/>
    </svg>

    <div class="brand-name"><span class="brand-name__dot"></span><span>The Wellness Barn</span></div>

    <div class="identity">
      <p class="identity__name">Carla Penhallow</p>
      <p class="identity__role">Physiotherapist</p>
      <p class="identity__address">4/37 Upper Creekbank Rd<br>Tallowbrook, QLD 4712</p>
    </div>

    <ul class="contacts">
      <li class="contacts__item">0462305178
        <svg class="contacts__icon" viewBox="0 0 24 24" aria-hidden="true"><path fill="currentColor" d="M6.6 10.8a15 15 0 0 0 6.6 6.6l2.2-2.2c.3-.3.7-.4 1-.2 1.1.4 2.3.6 3.6.6.6 0 1 .4 1 1V20c0 .6-.4 1-1 1A17 17 0 0 1 3 4c0-.6.4-1 1-1h3.5c.6 0 1 .4 1 1 0 1.3.2 2.5.6 3.6.1.3 0 .7-.2 1z"/></svg>
      </li>
      <li class="contacts__item">carlapenhallow57@mailbox.example
        <svg class="contacts__icon" viewBox="0 0 24 24" aria-hidden="true"><rect x="2" y="5" width="20" height="14" rx="2" fill="currentColor"/><path d="M3 6l9 7 9-7" fill="none" stroke="var(--paper)" stroke-width="1.8"/></svg>
      </li>
      <li class="contacts__item">www.thewellnessbarn.example.au
        <svg class="contacts__icon" viewBox="0 0 24 24" aria-hidden="true"><circle cx="12" cy="12" r="10" fill="currentColor"/><path d="M2 12h20M12 2c3 3 3 17 0 20M12 2c-3 3-3 17 0 20" fill="none" stroke="var(--paper)" stroke-width="1.4"/></svg>
      </li>
    </ul>
  </section>

  <section class="card card-back" aria-label="Business card back">
    <h2 class="appt-heading">APPOINTMENT<span class="appt-heading__rule"></span></h2>
    <div class="appt-row appt-row--name">
      <span class="appt-label">Name :</span><span class="appt-field"></span>
    </div>
    <div class="appt-row appt-row--when">
      <span class="appt-label">Date :</span><span class="appt-field"></span>
      <span class="appt-label appt-label--time">Time :</span><span class="appt-field"></span>
    </div>
    <ul class="day-list">
      <li class="day-list__item"><span class="day-list__box"></span>MON</li>
      <li class="day-list__item"><span class="day-list__box"></span>TUE</li>
      <li class="day-list__item"><span class="day-list__box"></span>WED</li>
      <li class="day-list__item"><span class="day-list__box"></span>THU</li>
      <li class="day-list__item"><span class="day-list__box"></span>FRI</li>
      <li class="day-list__item"><span class="day-list__box"></span>SAT</li>
    </ul>
  </section>

</main>
</body>
</html>
```